Consulting company (stride-and-calm, previously stundenfeld bremen) needs design for a clear and fre

This website is to be made completely new with Worpreess / Divi. I am at the beginning and have no idea about the design. The design is the focus of this order. After the first website I would like to use the design and colors for all other design products for business, which will be placed here as well.
On the website the services, the team, references ... should be separate pages. Please see the attached document. A very important part is the blog and the categories should be visible in the desktop view, vie widgets.

The site should be clear, well-arranged, but still convey freshness and vitality.
Our company offers consulting and online trainings for the following topics:
- Digital paperless office
- process optimization, digitalization
- Remote working and productivity
- Remote leadership
- remote project management
- Time management 4. 0
- Focus on the essentials

We do this in the form of:
- Keynote Speaking
- Facilitating
- Presentation
- Workshops and trainings
- Online trainings

Our services are intended exclusively for companies.

What drives us?
We want to inspire our customers to work more green, lean digital and focus on the essentials. We are a team of three people who are digital nomads, but who also work offline on site.
I do have already webseites, but they are old, but give you an idea what we do: stundenfeld-bremen.example.de. and ms-clearfile.example.com.

One style of a web site I like is for example is that of "plenvika.example.com" Colors I thought so far, but I'm not sure, could be the color palette "quarry bloom" from canva.com or something similar to # f60b80a and # 39dfa7. But I am open for other suggestions.
I love simple and clear fonts. I like this contemporary style of sites, where you get most of the content on the mobile devices by scrolling.

Target Market(s)

midsize and large businesses, decision maker

Logo Text

Let's work Stride and Calm

Number of Pages Required

5+ page

Font styles to use
Sans Serif

Colors
e34297
00a990

Requirements
Must have
• the page should be clear and concise, much white with color accents like content blocks or headlines, responsive,
Nice to have
• I like interesting backgrounds, very discreet, perhaps white and gray or the color shades of pastel, the site should somehow fit to the photos, the logo I added is the old one, just to give you an idea
Should not have
• in no case too playful or loud

```html
<!DOCTYPE html>
<html lang="en">
<head>
<meta charset="utf-8">
<title>Stride and Calm – Consulting</title>
<link rel="stylesheet" href="https://fonts.googleapis.com/css2?family=Montserrat:wght@400;500;600;700&family=Open+Sans:wght@400;600&display=swap">
<style>
:root{
  --teal:#00a990;
  --pink:#e34297;
  --ink:#2b2b2b;
  --text:#555;
  --muted:#888;
  --dark:#1c1c1c;
  --topbar:#2e2e2e;
  --gray:#f2f2f2;
  --line:#e2e2e2;
  --white:#fff;
}
*{box-sizing:border-box;margin:0;padding:0}
html,body{width:1200px;height:4941px;overflow:hidden}
body{position:relative;background:var(--white);font-family:"Open Sans",Arial,sans-serif;color:var(--text)}
.abs{position:absolute}
.heading{font-family:"Montserrat",Arial,sans-serif;font-weight:700;color:var(--ink);letter-spacing:2px;font-size:28px;text-align:center;width:1200px;left:0}
.heading span{display:inline-block;border-bottom:4px solid var(--teal);line-height:1.1;padding:0 2px}
/* top bar */
.topbar{top:0;left:0;width:1200px;height:34px;background:var(--topbar)}
.social-sq{width:34px;height:34px;border-right:1px solid #444;display:flex;align-items:center;justify-content:center}
.social-sq i{display:block;width:10px;height:10px;background:#bbb;border-radius:2px}
.topbar .contact{right:20px;top:0;height:34px;display:flex;gap:26px;align-items:center;color:#ccc;font-size:13px}
.topbar .contact span{display:flex;align-items:center;gap:6px}
/* nav */
.nav{top:34px;left:0;width:1200px;height:91px;background:var(--white);box-shadow:0 2px 6px rgba(0,0,0,.08)}
.brand{display:flex;align-items:center;gap:10px;font-family:"Montserrat",Arial,sans-serif;font-weight:600;font-size:28px;color:var(--teal)}
.brand .dot{width:44px;height:44px;border-radius:50%;background:var(--teal)}
.nav ul{list-style:none;position:absolute;right:24px;top:34px;display:flex;gap:36px;font-family:"Montserrat",Arial,sans-serif;font-size:15px;color:#333}
.nav li.active{color:var(--teal);border-bottom:2px solid var(--teal);padding-bottom:6px}
/* hero */
.hero-photo{top:125px;left:0;width:1200px;height:808px;background:linear-gradient(100deg,#cfd6db 0%,#e7ebee 45%,#b9c4c1 70%,#8a9b91 100%)}
.hero-box{top:391px;left:12px;width:621px;height:284px;background:rgba(25,25,25,.88);padding:26px 30px}
.hero-box h1{font-family:"Montserrat",Arial,sans-serif;font-weight:600;font-size:33px;letter-spacing:4px;color:var(--teal)}
.bar{width:56px;height:3px;background:var(--teal);margin:10px 0 20px}
.hero-box p{color:#eee;font-size:15px;line-height:22px}
.btn{display:inline-flex;align-items:center;gap:8px;background:var(--pink);color:#fff;font-family:"Montserrat",Arial,sans-serif;font-weight:500;font-size:15px;padding:0 18px;height:36px;border-radius:2px}
.hero-dots{top:897px;left:516px;display:flex;gap:10px}
.hero-dots i{display:block;width:50px;height:10px;border:2px solid #fff;border-radius:6px}
.hero-dots i.on{border-color:var(--teal)}
/* who we are */
.who-block{top:1077px;left:12px;width:458px;height:671px;background:var(--teal)}
.who-photo{top:1108px;left:42px;width:468px;height:679px;background:linear-gradient(180deg,#e8e8e6,#cfd0cc 60%,#b8b7b2)}
.who-text{top:1102px;left:565px;width:623px;font-size:15.5px;line-height:22px}
.who-text p{margin-bottom:22px}
.facility{top:1622px;left:468px;width:720px;height:214px;background:var(--teal);border-radius:0 0 6px 6px;padding:24px 56px;color:#fff}
.facility h3{font-family:"Montserrat",Arial,sans-serif;font-weight:400;font-size:36px}
.facility ul{list-style:none;display:grid;grid-template-columns:326px 300px;row-gap:10px;margin-top:18px;font-family:"Montserrat",Arial,sans-serif;font-size:18px}
.facility li:before{content:"›";margin-right:12px}
/* services */
.services-intro{top:2068px;left:40px;width:1120px;text-align:center;font-size:19px;line-height:27px;color:#444}
.card{background:#fff;box-shadow:0 1px 6px rgba(0,0,0,.15);text-align:center}
.svc{top:2205px;width:362px;height:230px;padding:80px 24px 0}
.svc h4{font-family:"Montserrat",Arial,sans-serif;font-weight:600;font-size:17px;letter-spacing:1px;color:#333;line-height:26px}
.svc .bar{margin:10px auto 16px;width:44px;height:2px}
.svc p{font-size:14.5px;color:var(--muted);line-height:20px}
.svc-icon{width:124px;height:124px;border-radius:50%;background:#fff;box-shadow:0 1px 6px rgba(0,0,0,.18);display:flex;align-items:center;justify-content:center;top:2146px}
.arrow-btn{top:2456px;width:40px;height:38px;border:2px solid var(--teal);background:#fff;display:flex;align-items:center;justify-content:center}
/* blog */
.blog-photo{top:2730px;width:362px;height:184px;background:linear-gradient(90deg,#d9dcdc,#f0f0ee 50%,#c9c7c0)}
.blog-card{top:2914px;width:334px;height:207px;text-align:left;padding:16px 12px}
.blog-card h5{font-family:"Montserrat",Arial,sans-serif;font-weight:500;font-size:18px;color:#333}
.blog-card .meta{font-size:11px;color:var(--muted);margin:4px 0 18px;line-height:17px}
.blog-card p{font-size:13px;color:var(--muted);line-height:20px}
.blog-card .more{color:var(--pink);font-family:"Montserrat",Arial,sans-serif;font-weight:600;font-size:14px;margin-top:10px}
/* testimonial */
.avatar{top:3438px;left:29px;width:172px;height:172px;border-radius:50%;background:linear-gradient(160deg,#e5e1dc,#b9aaa0);border:6px solid #fff;box-shadow:0 1px 6px rgba(0,0,0,.2)}
.quote{top:3472px;left:240px;width:940px;text-align:center;font-size:20px;line-height:27px;color:#333}
.who-name{top:3588px;left:240px;width:940px;text-align:center;font-family:"Montserrat",Arial,sans-serif}
.who-name b{display:block;color:var(--teal);font-weight:600;font-size:20px}
.who-name small{font-size:13px;color:#333;font-weight:600}
.t-dots{top:3665px;left:636px;display:flex;gap:10px}
.t-dots i{display:block;width:42px;height:10px;border:2px solid #333;border-radius:6px}
.t-dots i.on{border-color:var(--teal)}
/* map & form */
.map{top:3863px;left:42px;width:629px;height:402px;background:linear-gradient(135deg,#e9ecdf,#dfe7d4 50%,#d6e0e6);box-shadow:0 1px 6px rgba(0,0,0,.2)}
.stat{top:4013px;left:493px;width:178px;height:103px;background:var(--pink);color:#fff;text-align:center;padding-top:12px;font-family:"Montserrat",Arial,sans-serif}
.stat small{font-size:16px;font-weight:500}
.stat b{display:block;font-size:54px;font-weight:600;line-height:60px}
.form{top:3815px;left:669px;width:489px;height:498px;padding:22px 24px}
.form h3{font-family:"Montserrat",Arial,sans-serif;font-weight:700;font-size:24px;color:#333;display:inline-block;border-bottom:4px solid var(--teal);line-height:1.1}
.form label{display:block;text-align:left;font-size:13px;color:var(--muted);margin:28px 0 6px}
.form .field{height:36px;border:1px solid var(--line)}
.form .field.tall{height:116px}
.form .btn{margin-top:42px;padding:0 32px;font-weight:700;letter-spacing:1px}
/* footer */
.f-head{font-family:"Montserrat",Arial,sans-serif;font-size:25px;color:#fff;top:4550px}
.f-head:after{content:"";display:block;width:40px;height:3px;background:var(--pink);margin-top:8px}
.f-brand{top:4548px;left:14px;font-size:31px;color:#fff;font-weight:500}
.f-brand .dot{width:40px;height:40px;background:#fff}
.copy{top:4620px;left:22px;color:#ddd;font-size:13px}
.f-social{top:4700px;left:22px;display:flex;gap:12px}
.f-social i{display:block;width:36px;height:36px;border:2px solid var(--pink);border-radius:4px}
.f-nav{top:4618px;left:324px;list-style:none;color:#ddd;font-size:13px;line-height:26.2px}
.f-nav li:before{content:"›";margin-right:8px}
.tweet{left:577px;width:265px;font-size:11.5px;color:#ddd;line-height:17px;display:flex;gap:10px}
.tweet .tw{flex:none;width:12px;height:12px;border-radius:50%;background:var(--pink);margin-top:3px}
.tweet em{font-style:normal;color:var(--pink)}
.tweet .date{display:flex;justify-content:space-between;color:#aaa;font-size:11px}
.f-contact{left:918px;width:260px;color:#ddd;font-size:13px;line-height:19px;display:flex;gap:14px}
</style>
</head>
<body>

<!-- top bar -->
<div class="abs topbar">
  <div class="abs" style="left:0;top:0;display:flex">
    <div class="social-sq"><i></i></div><div class="social-sq"><i></i></div><div class="social-sq"><i></i></div><div class="social-sq"><i></i></div><div class="social-sq"><i></i></div>
  </div>
  <div class="abs contact">
    <span><svg width="12" height="12" viewBox="0 0 24 24"><path fill="#ccc" d="M6.6 10.8a15 15 0 0 0 6.6 6.6l2.2-2.2c.3-.3.7-.4 1-.2 1.1.4 2.3.6 3.6.6.6 0 1 .4 1 1V20c0 .6-.4 1-1 1A17 17 0 0 1 3 4c0-.6.4-1 1-1h3.5c.6 0 1 .4 1 1 0 1.3.2 2.5.6 3.6.1.3 0 .7-.2 1z"/></svg>+01 555 0100 24 68</span>
    <span><svg width="13" height="11" viewBox="0 0 26 20"><rect x="1" y="1" width="24" height="18" fill="none" stroke="#ccc" stroke-width="2"/><path d="M1 1l12 10L25 1" fill="none" stroke="#ccc" stroke-width="2"/></svg>info@strideandcalm.example.com</span>
  </div>
</div>

<!-- navigation -->
<header class="abs nav">
  <div class="abs brand" style="left:20px;top:22px"><span class="dot"></span>Stride and Calm</div>
  <ul>
    <li class="active">Home</li><li>About Us</li><li>Tips &amp; Trick</li><li>Services</li><li>Blog</li><li>Testimonials</li><li>Contact us</li>
  </ul>
</header>

<!-- hero -->
<div class="abs hero-photo" role="img" aria-label="Photo of a consultant in a green blazer working on a laptop in a bright office"></div>
<div class="abs hero-box">
  <h1>STRIDE AND CALM.</h1>
  <div class="bar"></div>
  <p>But I must explain to you how all this mistaken idea of denouncing pleasure and praising pain was born and I will give you a complete account of the system, and expound the actual teachings of the great explorer of the truth, the master-builder of human happiness.</p>
  <div class="btn" style="margin-top:26px">Read More <span>›</span></div>
</div>
<div class="abs hero-dots"><i></i><i class="on"></i><i></i></div>

<!-- who we are -->
<h2 class="abs heading" style="top:992px"><span>WHO WE ARE</span></h2>
<div class="abs who-block"></div>
<div class="abs who-photo" role="img" aria-label="Photo of a consultant in a checked suit walking down an office corridor"></div>
<div class="abs who-text">
  <p>At vero eos et accusamus et iusto odio dignissimos ducimus qui blanditiis praesentium voluptatum deleniti atque corrupti quos dolores et quas molestias excepturi sint occaecati cupiditate non provident, similique sunt in culpa qui officia deserunt mollitia animi, id est laborum et dolorum fuga. Et harum quidem rerum facilis est et expedita distinctio.</p>
  <p>But I must explain to you how all this mistaken idea of denouncing pleasure and praising pain was born and I will give you a complete account of the system, and expound the actual teachings of the great explorer of the truth, the master-builder of human happiness.</p>
  <p>Sed ut perspiciatis unde omnis iste natus error sit voluptatem accusantium doloremque laudantium, totam rem aperiam, eaque ipsa quae ab illo inventore veritatis et quasi architecto beatae vitae dicta sunt explicabo. Nemo enim ipsam voluptatem quia voluptas sit aspernatur aut odit aut fugit, sed quia consequuntur magni dolores eos qui ratione voluptatem sequi nesciunt.</p>
  <p>Similique sunt in culpa qui officia deserunt mollitia animi, id est laborum et dolorum fuga. Et harum quidem rerum facilis est et expedita distinctio.</p>
</div>
<div class="abs facility">
  <h3>Our Facility</h3>
  <ul><li>Keynote Speaking</li><li>Facilitating</li><li>Presentation</li><li>Workshops and trainings</li><li>Online trainings</li></ul>
</div>

<!-- services -->
<svg class="abs" style="top:0;left:0" width="1200" height="4941" aria-hidden="true">
  <polygon points="0,1895 1200,1945 1200,2620 0,2540" fill="#f2f2f2"/>
  <polygon points="0,3300 1200,3255 1200,3790 0,3800" fill="#f2f2f2"/>
  <path d="M0 4430 C 300 4470, 700 4330, 1200 4372" fill="none" stroke="#e34297" stroke-width="6"/>
  <path d="M0 4445 C 300 4485, 700 4345, 1200 4387 L1200 4941 L0 4941 Z" fill="#1c1c1c"/>
</svg>

<h2 class="abs heading" style="top:1995px"><span>OUR SERVICES</span></h2>
<p class="abs services-intro">Sed ut perspiciatis unde omnis iste natus error sit voluptatem accusantium doloremque laudantium, totam rem aperiam, eaque ipsa quae ab illo inventore veritatis et quasi architecto beatae vitae dicta sunt explicabo.</p>

<div class="abs card svc" style="left:27px"><h4>DIGITAL PAPERLESS OFFICE</h4><div class="bar"></div><p>Lorem ipsum dolor sit amet, consectetur adipiscing elit, sed do eiusmod tempor incididunt ut labore et dolore...</p></div>
<div class="abs card svc" style="left:418px"><h4>PROCESS OPTIMIZATION<br>DIGITALIZATION</h4><div class="bar"></div><p>Lorem ipsum dolor sit amet, consectetur adipiscing elit, sed do eiusmod tempor incididunt ut labore et dolore...</p></div>
<div class="abs card svc" style="left:809px"><h4>REMOTE WORKING<br>AND PRODUCTIVITY</h4><div class="bar"></div><p>Lorem ipsum dolor sit amet, consectetur adipiscing elit, sed do eiusmod tempor incididunt ut labore et dolore...</p></div>

<div class="abs svc-icon" style="left:146px"><svg width="50" height="58" viewBox="0 0 50 58"><path d="M4 2h30l12 12v42H4z" fill="none" stroke="#00a990" stroke-width="3"/><path d="M14 24h22M14 32h22M14 40h22M14 48h14" stroke="#00a990" stroke-width="3"/></svg></div>
<div class="abs svc-icon" style="left:537px"><svg width="64" height="64" viewBox="0 0 64 64" fill="none" stroke="#00a990" stroke-width="3"><circle cx="32" cy="24" r="14"/><circle cx="20" cy="44" r="12"/><circle cx="44" cy="44" r="12"/><path d="M20 38v12M44 38v12M32 18v12"/></svg></div>
<div class="abs svc-icon" style="left:928px"><svg width="64" height="64" viewBox="0 0 64 64" fill="none" stroke="#00a990" stroke-width="2.5"><circle cx="32" cy="32" r="10"/><rect x="4" y="4" width="12" height="12"/><rect x="48" y="4" width="12" height="12"/><rect x="4" y="48" width="12" height="12"/><rect x="48" y="48" width="12" height="12"/><path d="M16 16l9 9M48 16l-9 9M16 48l9-9M48 48l-9-9"/></svg></div>

<div class="abs arrow-btn" style="left:553px"><svg width="18" height="16" viewBox="0 0 18 16"><path d="M17 8H3M8 2L2 8l6 6" fill="none" stroke="#00a990" stroke-width="3"/></svg></div>
<div class="abs arrow-btn" style="left:605px"><svg width="18" height="16" viewBox="0 0 18 16"><path d="M1 8h14M10 2l6 6-6 6" fill="none" stroke="#00a990" stroke-width="3"/></svg></div>

<!-- blog -->
<h2 class="abs heading" style="top:2647px"><span>LATEST BLOG</span></h2>
<div class="abs blog-photo" style="left:27px" role="img" aria-label="Photo of a consultant in a pink top and dark blazer"></div>
<div class="abs blog-photo" style="left:418px" role="img" aria-label="Photo of a consultant standing in an office corridor"></div>
<div class="abs blog-photo" style="left:809px" role="img" aria-label="Photo of a consultant at a laptop in a bright office"></div>

<article class="abs card blog-card" style="left:40px"><h5>Time management 3.0</h5><div class="meta">Posted by Mira Elsen<br>▪ Jan 15, 2020 / ▫ Leave a Comment</div><p>Lorem ipsum dolor sit amet, consectetur ad-ipiscing elit, sed do eiusmod tempor incididunt ut labore et dolore..</p><div class="more">Read More ›</div></article>
<article class="abs card blog-card" style="left:431px"><h5>Focus on the essentials</h5><div class="meta">Posted by Mira Elsen<br>▪ Jan 25, 2020 / ▫ Leave a Comment</div><p>Lorem ipsum dolor sit amet, consectetur ad-ipiscing elit, sed do eiusmod tempor incididunt ut labore et dolore..</p><div class="more">Read More ›</div></article>
<article class="abs card blog-card" style="left:822px"><h5>Remote working and productivity</h5><div class="meta">Posted by Mira Elsen<br>▪ Jan 26, 2020 / ▫ Leave a Comment</div><p>Lorem ipsum dolor sit amet, consectetur ad-ipiscing elit, sed do eiusmod tempor incididunt ut labore et dolore..</p><div class="more">Read More ›</div></article>

<div class="abs btn" style="top:3152px;left:527px;width:146px;justify-content:center">View More ›</div>

<!-- testimonial -->
<h2 class="abs heading" style="top:3375px"><span>HAPPY CUSTOMER</span></h2>
<div class="abs avatar" role="img" aria-label="Portrait photo of the client"></div>
<p class="abs quote">Lorem ipsum dolor sit amet, consectetur adipiscing elit, sed do eiusmod tempor incididunt ut labore et dolore magna aliqua. Ut enim ad minim veniam, quis nostrud exercitation ullamco laboris nisi ut aliquip ex ea commodo consequat.</p>
<div class="abs who-name"><b>LENA OSTROW</b><small>CEO</small></div>
<div class="abs t-dots"><i></i><i class="on"></i><i></i></div>

<!-- map & form -->
<div class="abs map" role="img" aria-label="City map showing the office location"></div>
<div class="abs stat"><small>Satisfied Clients</small><b>126</b></div>
<form class="abs card form">
  <h3>Ask you Question</h3>
  <label>Name*</label><div class="field"></div>
  <label>Email*</label><div class="field"></div>
  <label>Message*</label><div class="field tall"></div>
  <div class="btn">SUBMIT</div>
</form>

<!-- footer -->
<div class="abs brand f-brand"><span class="dot"></span>Stride and Calm</div>
<p class="abs copy">Copyright © 2020 - Stride and Calm</p>
<div class="abs f-social"><i></i><i></i><i></i><i></i><i></i></div>

<h4 class="abs f-head" style="left:324px">Navigation</h4>
<ul class="abs f-nav">
  <li>Home</li><li>About Us</li><li>Tips &amp; Trick</li><li>Services</li><li>Blog</li><li>Testimonials</li><li>Contact us</li><li>Imprint</li><li>Mission Statement</li><li>Privacy Policy</li><li>Site Map</li>
</ul>

<h4 class="abs f-head" style="left:577px">Latest Tweets</h4>
<div class="abs tweet" style="top:4614px"><span class="tw"></span><div>But I must explain to you how all this mistaken idea of <em>denouncing pleasure.</em><div class="date"><span>♡ ⇄</span><span>Feb 12, 2020</span></div></div></div>
<div class="abs tweet" style="top:4693px"><span class="tw"></span><div>But I must explain to you how all this mistaken idea of <em>denouncing pleasure.</em><div class="date"><span>♡ ⇄</span><span>Feb 20, 2020</span></div></div></div>
<div class="abs tweet" style="top:4772px"><span class="tw"></span><div>But I must explain to you how all this mistaken idea of <em>denouncing pleasure.</em><div class="date"><span>♡ ⇄</span><span>Feb 26, 2020</span></div></div></div>
<div class="abs tweet" style="top:4851px"><span class="tw"></span><div>But I must explain to you how all this mistaken idea of <em>denouncing pleasure.</em><div class="date"><span>♡ ⇄</span><span>Feb 28, 2020</span></div></div></div>

<h4 class="abs f-head" style="left:918px">Contact Us</h4>
<div class="abs f-contact" style="top:4618px"><svg width="14" height="20" viewBox="0 0 14 20"><path d="M7 0a7 7 0 0 1 7 7c0 5-7 13-7 13S0 12 0 7a7 7 0 0 1 7-7z" fill="#e34297"/><circle cx="7" cy="7" r="2.5" fill="#1c1c1c"/></svg><span>12 Example Lane, West Harbor, FL 00000</span></div>
<div class="abs f-contact" style="top:4678px"><svg width="16" height="16" viewBox="0 0 24 24"><path fill="#e34297" d="M6.6 10.8a15 15 0 0 0 6.6 6.6l2.2-2.2c.3-.3.7-.4 1-.2 1.1.4 2.3.6 3.6.6.6 0 1 .4 1 1V20c0 .6-.4 1-1 1A17 17 0 0 1 3 4c0-.6.4-1 1-1h3.5c.6 0 1 .4 1 1 0 1.3.2 2.5.6 3.6.1.3 0 .7-.2 1z"/></svg><span>+01 555 0100 24 68</span></div>
<div class="abs f-contact" style="top:4720px"><svg width="16" height="13" viewBox="0 0 26 20"><rect x="1" y="1" width="24" height="18" fill="none" stroke="#e34297" stroke-width="2.5"/><path d="M1 1l12 10L25 1" fill="none" stroke="#e34297" stroke-width="2.5"/></svg><span>info@strideandcalm.example.com</span></div>

</body>
</html>
```